High End Clothing Line Needs Stationary Design

We need a stationery design including letterhead and envelopes for a new Christian clothing company called Harborlight 4 based out of New York. Our company colors are charcoal gray and silver. The final design needs to be modern, simple, and have a high end look to it.

Industry/Entity Type

Clothing

Font styles to use
Sans Serif

Colors
474747
cfcfcf

Requirements
Must have
• On the top of page in center we would like a dark gray solid box with logo inside in light gray. Name, email, title, phone # must be on bottom of the page.
• Light gray cross will be on black flap of envelope. Entire back flap in dark gray. Eventually logo and cross will be done in silver stamping when project complete.
Nice to have
• Would like to see how just the logo without Harborlight 4 looks in middle of letterhead faded in background.

```html
<!DOCTYPE html>
<html lang="en">
<head>
<meta charset="utf-8">
<title>Harborlight 4 — Business Card</title>
<link rel="stylesheet" href="https://fonts.googleapis.com/css2?family=Jost:wght@400;500;600&display=swap">
<style>
  :root {
    --backdrop: #e4e5e7;
    --charcoal: #1f1f1e;
    --charcoal-soft: #474747;
    --silver: #cfcfcf;
    --silver-light: #dcdcdc;
    --paper: #ffffff;
    --ink: #1a1a1a;
  }
  * { box-sizing: border-box; margin: 0; padding: 0; }
  html, body {
    width: 1200px;
    height: 1000px;
    overflow: hidden;
    background: var(--backdrop);
    font-family: "Jost", "Futura", sans-serif;
  }
  .stationery {
    position: relative;
    width: 1200px;
    height: 1000px;
    display: flex;
    justify-content: center;
    align-items: center;
    gap: 90px;
  }
  .card {
    position: relative;
    width: 320px;
    height: 560px;
    overflow: hidden;
    box-shadow: 0 10px 28px rgba(0, 0, 0, 0.12);
  }

  /* Front: solid charcoal with the wordmark */
  .card--front {
    background: var(--charcoal);
    display: flex;
    align-items: center;
    justify-content: center;
  }
  .wordmark {
    color: var(--silver);
    font-weight: 500;
    font-size: 30px;
    letter-spacing: 0.08em;
    text-transform: uppercase;
    white-space: nowrap;
  }

  /* Back: charcoal top, silver band, white contact panel */
  .card--back { background: var(--paper); }
  .card-back__shape {
    position: absolute;
    inset: 0;
    width: 100%;
    height: 100%;
  }
  .card-back__brand {
    position: absolute;
    left: 0;
    right: 0;
    top: 120px;
    text-align: center;
  }
  .card-back__brand .wordmark { font-size: 26px; }

  .contact {
    position: absolute;
    left: 44px;
    top: 330px;
    color: var(--ink);
    font-size: 15px;
    line-height: 1.35;
  }
  .contact__name {
    font-weight: 600;
    font-size: 19px;
    letter-spacing: 0.03em;
    text-transform: uppercase;
  }
  .contact__title { margin-bottom: 6px; }
  .contact__label { font-weight: 600; }
  .contact__address { margin-top: 16px; }
</style>
</head>
<body>
<main class="stationery">

  <section class="card card--front" aria-label="Business card front">
    <span class="wordmark">Harborlight 4</span>
  </section>

  <section class="card card--back" aria-label="Business card back">
    <svg class="card-back__shape" viewBox="0 0 320 560" preserveAspectRatio="none" aria-hidden="true">
      <path d="M0 0 H320 V300 C250 300 230 230 160 245 C90 260 70 300 0 300 Z" fill="var(--silver)"/>
      <path d="M0 0 H320 V286 C250 286 225 218 160 232 C92 246 70 286 0 286 Z" fill="var(--charcoal)"/>
      <path d="M0 300 C70 300 90 260 160 245 C230 230 250 300 320 300 V314 C250 314 232 246 160 260 C92 274 70 314 0 314 Z" fill="var(--silver-light)"/>
    </svg>

    <div class="card-back__brand">
      <span class="wordmark">Harborlight 4</span>
    </div>

    <div class="contact">
      <p class="contact__name">Jordan Ellis</p>
      <p class="contact__title">General Manager</p>
      <p><span class="contact__label">T:</span> 555.010.4821</p>
      <p><span class="contact__label">E:</span> info@harborlight4.com</p>
      <p><span class="contact__label">W:</span> www.harborlight4.com</p>
      <p class="contact__address">22 Pier Avenue<br>9th Street, Suite 4</p>
    </div>
  </section>

</main>
</body>
</html>
```